Opening Specials Flyer for SmileHaven Dental

We require a flyer design for our promotions/special offers for our new opening of Dental Practice. Please make one page flyer with designs on front and back
Opening Specials must be eye catchy, with images
FRONT - OPENING SPECIALS
BACK - MAP and Introduce our NEW CLINIC
on Back - MUST SAY "FLIP BACK OF FLYER TO VIEW OPENING SPECIAL OFFERS"

Opening specials to our local residents of West Ryde

Colour Scheme: Green, grey, white
Celebrate the opening of our new clinic
Opening Specials for West Ryde Residents include:

1. NO GAP Checkup for the whole family
NO GAP - Checkup Clean Fluoride X-rays - (to eligible health fund members)
2. Dental Crowns at half price - Full Ceramic $900 (includes core and crown, root canal extra) (please use picture of ceramic crown attached) - must bring voucher/flyer
3. Power tooth Whitening (Corvel Glint)- $400 must bring voucher/flyer
1hr office in chair whitening, immediate whitening results
4. 20% off all General Dental Treatment (must bring flyer- please design this onto flyer)
5. Free Healthcover Dental for Kids (for those eligible under Junior Oral Care Program up to $1000) - please have healthcover logo
6. Free consultation for second opinion of treatment plans

Emergency dental care available after hours, please contact (02) 7395 2268

Offer valid until 31st May 2016
by appointment only
No Gap for eligible health fund members only
Address: Shop 7/51-53 Larkin Rd West Ryde 2114
Please have image of atlas view of this location

Behind the flyer (back) I would like to introduce our new clinic:
MUST INCLUDE - Flip behind for opening special offers!

SmileHaven Dental is your Local Family Dentist
Newly opened in March 2016, we aim to provide local residents with affordable dentistry with a gentle friendly approach. We are a child friendly practice and welcome you and your family to visit our new clinic.

www.smilehavenclinic.com.au
info@smilehavenclinic.com.au
(02) 7395 2268

Target Market(s)

Residents of West Ryde and Surrounding Suburbs
Children and Family

Industry/Entity Type

Dental Clinic

Colors
acd036
b2b2b2

Requirements
Must have
• (You may phrase as you please)
• Newly Opened Dental Clinic in West Ryde
• Special Offers until 31st May 2016
• Specials and clearly big font "NO GAP"
• Healthcover logo (colour) next to "Free Healthcover Dental for Kids
• MUST have SmileHaven Dental Logo
• Must inform that voucher must be brought in order to claim specials
• Must have address: Shop 7/51-53 Larkin Rd West Ryde 2114
• Must have Ph: (02) 7395 2268
Nice to have
• Image of dental crown - full ceramic (attached)
• Image of Corvel Glint Whitening
• Map of Shop 7/51-53 Larkin Rd West Ryde (Atlas View)
• Happy family picture

```html
<!DOCTYPE html>
<html lang="en">
<head>
<meta charset="utf-8">
<title>SmileHaven Dental – Opening Specials</title>
<link rel="stylesheet" href="https://fonts.googleapis.com/css2?family=Montserrat:wght@800&family=Open+Sans:ital,wght@0,400;0,600;0,700;1,400;1,600;1,700&family=Roboto+Condensed:wght@400&display=swap">
<style>
  :root {
    --green: #acd036;
    --green-deep: #8dba1f;
    --green-text: #9cc62b;
    --grey: #b2b2b2;
    --charcoal: #3d3d3f;
    --charcoal-dark: #2b2b2c;
    --text-dark: #444446;
    --white: #ffffff;
  }
  * { margin: 0; padding: 0; box-sizing: border-box; }
  html, body { width: 902px; height: 1200px; overflow: hidden; background: var(--white); }
  body { font-family: "Open Sans", Arial, sans-serif; color: var(--text-dark); }

  .flyer { position: relative; width: 902px; height: 1200px; overflow: hidden; background: var(--white); }

  .hero-photo {
    position: absolute; left: 0; top: 0; width: 902px; height: 560px;
    background:
      radial-gradient(ellipse at 30% 40%, rgba(240,230,215,.9), transparent 45%),
      radial-gradient(ellipse at 70% 55%, rgba(110,160,210,.85), transparent 40%),
      linear-gradient(160deg, #dfeec2 0%, #a7cf5a 45%, #7fae3a 100%);
  }
  .hero-waves { position: absolute; left: 0; top: 0; width: 902px; height: 620px; }

  .brand { position: absolute; left: 40px; top: 545px; display: flex; align-items: center; gap: 12px; }
  .brand-dot { width: 30px; height: 30px; border-radius: 50%; background: var(--green); }
  .brand-name { font-weight: 600; color: #6d6e70; font-size: 36px; line-height: 1.05; }

  .headline {
    position: absolute; right: 42px; top: 560px;
    font-family: "Montserrat", Arial, sans-serif; font-weight: 800; font-size: 108px;
    letter-spacing: 1px; line-height: 1; color: var(--charcoal);
  }
  .headline .accent { color: var(--green); }
  .headline-sub {
    position: absolute; right: 42px; top: 682px; text-align: right;
    font-style: italic; font-weight: 700; font-size: 23px; line-height: 32px; color: #5a5a5c;
  }

  .offer-pill {
    position: absolute; left: 0; top: 772px; width: 317px; height: 99px;
    background: linear-gradient(180deg, #4a4a4c, var(--charcoal-dark));
    border-radius: 0 50px 50px 0; padding: 8px 0 0 28px;
    font-family: "Roboto Condensed", Arial, sans-serif; line-height: 1;
  }
  .offer-pill .lead { color: var(--green); font-size: 37px; display: block; }
  .offer-pill .date { color: var(--white); font-size: 44px; display: block; margin-top: 6px; }

  .terms { position: absolute; left: 29px; top: 895px; font-size: 13px; line-height: 18px; color: #444; }

  .emergency { position: absolute; left: 29px; top: 970px; font-weight: 600; font-size: 21px; line-height: 26px; text-transform: uppercase; color: var(--text-dark); }
  .emergency .hl { color: var(--green-text); }

  .contact-lead { position: absolute; left: 29px; top: 1036px; font-style: italic; font-weight: 600; font-size: 19px; color: var(--green-text); }
  .phone { position: absolute; left: 29px; top: 1068px; display: flex; align-items: center; gap: 14px; font-weight: 700; font-size: 41px; line-height: 52px; color: var(--text-dark); }
  .phone svg { width: 30px; height: 30px; }

  .bring-flyer {
    position: absolute; left: 22px; top: 1128px; width: 190px; height: 28px;
    border: 1.5px dashed var(--green); border-radius: 14px;
    font-weight: 600; font-size: 15px; line-height: 25px; text-align: center; color: #333;
  }

  .specials-panel {
    position: absolute; left: 420px; top: 772px; width: 482px; height: 393px;
    background: linear-gradient(90deg, #bcdc48 0%, var(--green) 40%, var(--green-deep) 100%);
  }
  .specials-photo {
    position: absolute; width: 124px; height: 124px; border-radius: 50%;
    border: 5px solid var(--green); box-shadow: 0 0 0 4px var(--white), 0 3px 8px rgba(0,0,0,.35);
  }
  .specials-photo.crown { left: 356px; top: 778px; background: radial-gradient(circle at 45% 45%, #ffffff, #e8e2d6 50%, #c9b9a2 100%); }
  .specials-photo.whitening { left: 356px; top: 914px; background: radial-gradient(circle at 50% 45%, #f5dccb, #e2b9a0 55%, #cfd4d8 100%); }
  .specials-photo.kids { left: 356px; top: 1036px; background: radial-gradient(circle at 50% 45%, #f2d5c2, #c99a78 55%, #f1f1f1 100%); }

  .special-tag {
    position: absolute; right: 0; height: 26px; padding: 0 36px 0 18px;
    background: var(--white); border-radius: 13px 0 0 13px;
    font-weight: 700; font-size: 13px; line-height: 26px; text-transform: uppercase; color: #333;
  }
  .special-detail { position: absolute; right: 36px; text-align: right; color: var(--white); font-size: 12px; line-height: 18px; }
  .special-detail.strong { font-weight: 700; font-size: 14px; }
  .special-detail.note { font-style: italic; color: #2f3a10; font-weight: 600; }

  .partner-badge { position: absolute; left: 508px; top: 1029px; width: 72px; height: 22px; background: #1d8a4a; border-radius: 3px; border: 2px solid var(--white); }

  .site-footer {
    position: absolute; left: 0; top: 1165px; width: 902px; height: 35px;
    background: linear-gradient(180deg, #3a3a3b, #1f1f20);
    color: var(--white); font-weight: 600; font-size: 14px; letter-spacing: 2px; line-height: 35px; text-align: center;
  }
  .site-footer .sep { color: var(--green); margin: 0 12px; }
</style>
</head>
<body>
<main class="flyer">
  <div class="hero-photo" role="img" aria-label="Happy family of four smiling together outdoors in a sunny green park"></div>
  <svg class="hero-waves" viewBox="0 0 902 620" aria-hidden="true">
    <defs>
      <linearGradient id="waveDark" x1="0" y1="0" x2="0" y2="1">
        <stop offset="0" stop-color="#4a4a4c"/><stop offset="1" stop-color="#1f1f20"/>
      </linearGradient>
      <linearGradient id="waveGreen" x1="0" y1="0" x2="1" y2="0">
        <stop offset="0" stop-color="#c8e25a"/><stop offset="1" stop-color="#8dba1f"/>
      </linearGradient>
    </defs>
    <path d="M0 326 C 150 300, 300 330, 460 420 C 570 482, 720 470, 902 420 L902 620 L0 620 Z" fill="url(#waveDark)"/>
    <path d="M0 434 C 180 440, 330 520, 520 540 C 680 556, 800 540, 902 536 L902 620 L0 620 Z" fill="#ffffff"/>
    <path d="M470 474 C 610 486, 770 446, 902 386 L902 494 C 780 516, 620 522, 470 474 Z" fill="url(#waveGreen)"/>
  </svg>

  <div class="brand">
    <span class="brand-dot"></span>
    <span class="brand-name">SmileHaven<br>Dental</span>
  </div>

  <h1 class="headline">NO <span class="accent">GAP</span></h1>
  <p class="headline-sub">NO GAP - Checkup Clean Fluoride X-rays<br>(to eligible health fund members)</p>

  <div class="offer-pill">
    <span class="lead">Offer valid until</span>
    <span class="date">31ST MAY 2016</span>
  </div>

  <p class="terms">by appointment only<br>No Gap for eligible health fund members only</p>

  <p class="emergency">Emergency dental care<br><span class="hl">available after hours</span></p>
  <p class="contact-lead">Please contact</p>
  <p class="phone">
    <svg viewBox="0 0 24 24" aria-hidden="true"><path fill="#acd036" d="M6.6 10.8a15.1 15.1 0 0 0 6.6 6.6l2.2-2.2c.3-.3.7-.4 1-.2 1.1.4 2.3.6 3.6.6.6 0 1 .4 1 1V20c0 .6-.4 1-1 1A17 17 0 0 1 3 4c0-.6.4-1 1-1h3.5c.6 0 1 .4 1 1 0 1.3.2 2.5.6 3.6.1.3 0 .7-.2 1z"/></svg>
    02 7395 2268
  </p>
  <p class="bring-flyer">Must bring flyer</p>

  <section class="specials-panel" aria-label="Opening specials"></section>

  <div class="specials-photo crown" role="img" aria-label="Full ceramic dental crown and implant illustration"></div>
  <div class="specials-photo whitening" role="img" aria-label="Woman with bright white smile after tooth whitening"></div>
  <div class="specials-photo kids" role="img" aria-label="Smiling young girl with pigtails"></div>

  <p class="special-tag" style="top:804px">Dental crowns at half price</p>
  <p class="special-detail strong" style="top:840px">Full Ceramic $900</p>
  <p class="special-detail" style="top:862px">(includes core and crown, root canal extra) or no GAP if<br>Crown is covered by health insurance</p>

  <p class="special-tag" style="top:914px">Power tooth whitening</p>
  <p class="special-detail strong" style="top:948px">(Corvel Glint)- $400</p>

  <p class="special-tag" style="top:981px">20% off all general dental treatment</p>

  <span class="partner-badge" aria-hidden="true"></span>
  <p class="special-tag" style="top:1027px">Free Healthcover dental for kids</p>
  <p class="special-detail note" style="top:1058px">(for those eligible under Junior Oral Care Program<br>up to $1000)</p>

  <p class="special-tag" style="top:1106px">Free consultation</p>
  <p class="special-detail note" style="top:1138px">For second opinion of treatment plans</p>

  <footer class="site-footer">Shop 7/51-53 Larkin Rd West Ryde 2114<span class="sep">|</span>www.smilehavenclinic.com.au</footer>
</main>
</body>
</html>
```